Hard-File Archival Services Billboard (Digitization Service) for Attorneys/Law Firms

I need a billboard design for my company "Keltor Legal Aides" that advertises our primary service: Digitization of closed client files, for law firms and attorneys. Our system works as follows: 1) We get a call about a firm that wants to digitize their archived (closed) client files (which usually find their way to file cabinets or bankers boxes), 2) We go and pick those up from the law firm, 3) We bring them to our digitization facility, scan them in, and convert them into searchable PDF/A files, and 4) We upload them on the cloud, give the client a URL to visit their files whenever they want, and we delete them when requested by the client (usually for the retention duration for Missouri's rules of professional conduct, which is 6 years). It would be really cool to see "Keltor Legal Aides" and the logo clearly on the billboard, some simple sentence relating to "Missouri's best digitizing and cloud storage service for closed client files for attorneys" (or something shorter, you get the point), with maybe a linear set of photos and arrows (as follows 1. A photo of a file cabinet opened with files hanging out of it, 2. an arrow pointing to a person scanning in documents in a big scanner (maybe with a Keltor Legal Aidess logo on it?), 3. An arrow pointing to a "secure" appearing cloud (representing cloud storage), and 4. the client sitting at a computer with an arrow pointing back to the cloud (showing the client is accessing the cloud files through the computer). Our website is www.keltorlegalaides.example if you want to glean any additional information from there. Thanks! Oh yes, I should also say the billboard dimensions (in the event you need this for photo aspect ratio) will be as follows: 14 feet tall by 48 feet wide.
Target Market(s)
Attorneys in Springfield, Missouri
Industry/Entity Type
Legal
Look and feel
Each slider illustrates characteristics of the customer's brand and the style your logo design should communicate.

```html
<!DOCTYPE html>
<html lang="en">
<head>
<meta charset="utf-8">
<title>Keltor Legal Aides – Billboard</title>
<link rel="stylesheet" href="https://fonts.googleapis.com/css2?family=Oswald:wght@500;600;700&family=Roboto+Condensed:wght@300&family=Archivo:wght@500;700&display=swap">
<style>
  :root {
    --backdrop: #7d7d7d;
    --paper: #ffffff;
    --ink: #1e1e20;
    --band: #232326;
    --slate: #8a8a8c;
    --pill: #6f6f72;
    --arrow: #f2373c;
    --violet: #b46fc4;
    --violet-soft: #eab7e6;
    --teal-dark: #2f4b4f;
  }
  * { box-sizing: border-box; margin: 0; padding: 0; }
  html, body { width: 1094px; height: 1200px; overflow: hidden; }
  body { background: var(--backdrop); position: relative; }

  .billboard {
    position: absolute; left: 27px; top: 449px;
    width: 1040px; height: 302px;
    background: var(--paper);
    box-shadow: 0 6px 18px rgba(0,0,0,.35);
    overflow: hidden;
  }

  .headline-band { position: absolute; inset: 0; }

  .brand-title {
    position: absolute; left: 268px; top: 11px;
    font-family: "Oswald", sans-serif; font-weight: 600;
    font-size: 43px; line-height: 60px; color: #fff;
    letter-spacing: -0.5px; white-space: nowrap;
  }
  .partner-pill {
    position: absolute; left: 627px; top: 25px; width: 390px; height: 42px;
    background: var(--pill); border-radius: 6px;
    font-family: "Roboto Condensed", sans-serif; font-weight: 300;
    font-size: 21px; color: #fff; line-height: 42px; text-align: center;
    white-space: nowrap;
  }

  .brand-mark {
    position: absolute; left: 26px; top: 48px;
    display: flex; align-items: center; gap: 8px;
  }
  .brand-mark .dot { width: 26px; height: 26px; border-radius: 50%; background: var(--ink); }
  .brand-mark .name {
    font-family: "Oswald", sans-serif; font-weight: 600;
    font-size: 34px; color: var(--ink); letter-spacing: 1px;
  }

  .tagline {
    position: absolute; left: 26px; top: 150px;
    font-family: "Archivo", sans-serif; font-weight: 500;
    font-size: 18px; line-height: 23px; color: var(--ink);
    white-space: nowrap;
  }
  .service {
    position: absolute; left: 25px; top: 198px;
    font-family: "Oswald", sans-serif; font-weight: 600;
    font-size: 38px; line-height: 42px; letter-spacing: -0.8px;
    white-space: nowrap;
  }
  .service span { display: block; transform-origin: left center; }
  .service .line-one { color: var(--slate); }
  .service .line-two { color: var(--ink); transform: scaleX(0.83); }

  .process { position: absolute; left: 0; top: 0; width: 100%; height: 100%; pointer-events: none; }
  .step { position: absolute; border-radius: 6px; }
  .step-cabinet { left: 318px; top: 92px; width: 92px; height: 145px;
    background: linear-gradient(135deg, var(--teal-dark) 0 45%, var(--violet-soft) 100%); }
  .step-scanner { left: 495px; top: 98px; width: 131px; height: 139px;
    background: linear-gradient(160deg, var(--violet) 0 50%, var(--violet-soft) 100%); }
  .step-cloud { left: 692px; top: 94px; width: 94px; height: 143px;
    background: linear-gradient(180deg, var(--violet-soft), #c9c9d2); }
  .step-desk { left: 847px; top: 92px; width: 170px; height: 148px;
    background: linear-gradient(150deg, #d7d7dd 0 35%, var(--violet-soft) 100%); }

  .phone-tab {
    position: absolute; left: 307px; top: 252px; width: 293px; height: 33px;
    background: var(--band); border-radius: 6px 0 0 6px;
    display: flex; align-items: center; gap: 8px; padding-left: 18px;
    font-family: "Archivo", sans-serif; font-weight: 700;
    font-size: 21px; color: #fff; letter-spacing: 0.5px; white-space: nowrap;
  }
  .web-tab {
    position: absolute; left: 604px; top: 252px; width: 436px; height: 33px;
    background: var(--slate);
    font-family: "Archivo", sans-serif; font-weight: 700;
    font-size: 17px; color: #fff; letter-spacing: 3.6px;
    line-height: 33px; padding-left: 18px; white-space: nowrap;
  }
</style>
</head>
<body>
  <main class="billboard">
    <svg class="headline-band" width="1040" height="302" viewBox="0 0 1040 302" aria-hidden="true">
      <polygon points="180,0 202,0 248,82 226,82" fill="var(--slate)"/>
      <polygon points="212,0 1040,0 1040,82 258,82" fill="var(--band)"/>
    </svg>

    <div class="brand-title">KELTOR LEGAL AIDES</div>
    <div class="partner-pill">POWERED BY VANTIRO CLOUD SERVICES</div>

    <div class="brand-mark">
      <span class="dot"></span>
      <span class="name">KELTOR</span>
    </div>

    <p class="tagline">TOP MISSOURI<br>SERVICE FOR ATTORNEY</p>
    <h1 class="service">
      <span class="line-one">FILE DIGITIZATION</span>
      <span class="line-two">AND CLOUD STORAGE</span>
    </h1>

    <div class="step step-cabinet" role="img" aria-label="Illustration of an open file cabinet full of archived client files"></div>
    <div class="step step-scanner" role="img" aria-label="Illustration of a person scanning documents on a large scanner"></div>
    <div class="step step-cloud" role="img" aria-label="Illustration of a person on a server stack uploading files to a secure cloud"></div>
    <div class="step step-desk" role="img" aria-label="Illustration of a client at a desk accessing files on a laptop"></div>

    <svg class="process" width="1040" height="302" viewBox="0 0 1040 302" aria-hidden="true">
      <g fill="none" stroke="var(--arrow)" stroke-width="7" stroke-linecap="round">
        <path d="M424 144 Q448 114 474 122"/>
        <path d="M620 144 Q644 112 670 122"/>
        <path d="M840 146 Q818 116 798 124"/>
      </g>
      <g fill="var(--arrow)">
        <polygon points="488,124 468,110 470,134"/>
        <polygon points="684,124 664,110 666,134"/>
        <polygon points="786,126 804,112 804,136"/>
      </g>
    </svg>

    <div class="phone-tab">
      <svg width="20" height="20" viewBox="0 0 20 20" aria-hidden="true">
        <circle cx="10" cy="10" r="9.5" fill="#8a8a8c"/>
        <path d="M6.5 5 L8.5 5 L9.3 7.6 L8 8.6 Q9 11 11.4 12 L12.4 10.7 L15 11.5 L15 13.5 Q14 15 12 14.6 Q6.8 13 5.4 7.8 Q5.2 5.8 6.5 5 Z" fill="#fff"/>
      </svg>
      <span>+1 (417) 555-0184</span>
    </div>
    <div class="web-tab">www.keltorlegalaides.example</div>
  </main>
</body>
</html>
```